Looking for awesome business card design with attached existing logo

We are a water, mold, and fire damage restoration company called "Torvane Seco" Looking for an awesome business card that is edgy yet professional and unique. Show me what you got!

```html
<!DOCTYPE html>
<html lang="en">
<head>
<meta charset="utf-8">
<title>Torvane Seco – Business Card</title>
<link href="https://fonts.googleapis.com/css2?family=Montserrat:wght@400;500;700;800&display=swap" rel="stylesheet">
<style>
  :root {
    --stage: #2b2b2d;
    --teal: #2c4a56;
    --gold: #d49a1f;
    --white: #ffffff;
    --ink: #2a2a2a;
    --faint-gold: rgba(212, 154, 31, 0.08);
  }
  * { margin: 0; padding: 0; box-sizing: border-box; }
  html, body {
    width: 1200px; height: 1186px; overflow: hidden;
    background: var(--stage);
    font-family: "Montserrat", sans-serif;
  }
  .card {
    position: absolute; left: 80px;
    width: 1040px; height: 540px;
    border-radius: 28px; overflow: hidden;
  }
  .card-front { top: 40px; background: var(--teal); }
  .card-back { top: 606px; background: var(--white); }

  .front-mark-bg {
    position: absolute; right: 90px; top: 30px;
    width: 300px; height: 300px; border-radius: 50%;
    background: rgba(255,255,255,0.04);
  }
  .brand {
    display: flex; align-items: center; gap: 18px;
    font-weight: 800; letter-spacing: 1px;
  }
  .brand-dot { border-radius: 50%; background: var(--gold); flex: none; }
  .brand-front {
    position: absolute; left: 0; right: 0; top: 220px;
    justify-content: center; color: var(--white); font-size: 84px;
  }
  .brand-front .brand-dot { width: 46px; height: 46px; }

  .back-mark-bg {
    position: absolute; left: 90px; top: 80px;
    width: 360px; height: 360px; border-radius: 50%;
    background: var(--faint-gold);
  }
  .brand-back {
    position: absolute; right: 70px; top: 70px;
    color: var(--teal); font-size: 52px;
  }
  .brand-back .brand-dot { width: 30px; height: 30px; }
  .divider {
    position: absolute; left: 60px; right: 70px; top: 290px;
    height: 2px; background: var(--gold);
  }
  .address {
    position: absolute; right: 70px; top: 222px;
    text-align: right; font-size: 20px; line-height: 1.3; color: var(--ink);
  }
  .person { position: absolute; left: 60px; top: 318px; }
  .person-name { font-weight: 700; font-size: 34px; color: var(--gold); }
  .person-role { font-size: 20px; color: var(--ink); margin-top: 2px; }
  .contacts {
    position: absolute; left: 60px; top: 408px;
    list-style: none; font-size: 21px; color: var(--ink);
  }
  .contacts li { display: flex; align-items: center; gap: 14px; height: 34px; }
  .contacts svg { width: 20px; height: 20px; fill: var(--gold); flex: none; }
</style>
</head>
<body>
  <section class="card card-front">
    <div class="front-mark-bg"></div>
    <div class="brand brand-front"><span class="brand-dot"></span>Torvane Seco</div>
  </section>

  <section class="card card-back">
    <div class="back-mark-bg"></div>
    <div class="brand brand-back"><span class="brand-dot"></span>Torvane Seco</div>
    <p class="address">Kornmarkt 58<br>20457 Hamburg</p>
    <div class="divider"></div>
    <div class="person">
      <p class="person-name">Aldo Brenner</p>
      <p class="person-role">Owner</p>
    </div>
    <ul class="contacts">
      <li>
        <svg viewBox="0 0 24 24"><path d="M6.6 10.8a15 15 0 0 0 6.6 6.6l2.2-2.2a1 1 0 0 1 1-.25 11.4 11.4 0 0 0 3.6.57 1 1 0 0 1 1 1V20a1 1 0 0 1-1 1A17 17 0 0 1 3 4a1 1 0 0 1 1-1h3.5a1 1 0 0 1 1 1c0 1.25.2 2.45.57 3.57a1 1 0 0 1-.25 1z"/></svg>
        +49 40 555 0182
      </li>
      <li>
        <svg viewBox="0 0 24 24"><path d="M2 5h20v14H2z M2 5l10 8 10-8" fill="none" stroke="#d49a1f" stroke-width="2"/></svg>
        info@torvaneseco.com
      </li>
      <li>
        <svg viewBox="0 0 24 24"><circle cx="12" cy="12" r="9" fill="none" stroke="#d49a1f" stroke-width="2"/><path d="M3 12h18M12 3c3 3 3 15 0 18M12 3c-3 3-3 15 0 18" fill="none" stroke="#d49a1f" stroke-width="1.6"/></svg>
        www.torvaneseco.com
      </li>
    </ul>
  </section>
</body>
</html>
```